Carton Box Packaging For Motorcycle Brake Shoe - Vorenta Brand

Packaging Dimensions: 125mm (H) x 125mm (W) x 31mm (D)
We would like to design a genuine Carton box Packaging for motorcycle Brake Shoe.
This is a critical part of the motorcycle, so we need the packaging to reflect elegant impression.
Vorenta, is one of the leading companies for manufacturing Motorcycles, located in Egypt. Our company is offering high-quality products, the best in the local market, with very competitive prices.
We have a limited time to get this project done, So we Highly appreciate receiving your designs ASAP.
Target Market(s)
Economical Motorcycle Buyers
Font styles to use
Colors
Designer to choose colors to be used in the design.
Look and feel
Each slider illustrates characteristics of the customer's brand and the style your logo design should communicate.

```html
<!DOCTYPE html>
<html lang="en">
<head>
<meta charset="utf-8">
<title>Vorenta Motorcycle Brake Shoes – Carton Side and Front Panels</title>
<link rel="stylesheet" href="https://fonts.googleapis.com/css2?family=Audiowide&family=Roboto+Condensed:wght@700&display=swap">
<style>
  :root {
    --stage: #5f5f5f;
    --panel-dark: #161616;
    --panel-mid: #3a3a3a;
    --silver: #d9d9d9;
    --label-yellow: #f2e21c;
    --label-ink: #111111;
    --banner-red: #c4142a;
    --banner-red-dark: #7d0d1b;
    --banner-blue: #1f2f8f;
    --banner-blue-dark: #0d1552;
    --white: #ffffff;
    --shoe-light: #b9b4a6;
    --shoe-dark: #6f6a5e;
    --fold: #0a0a0a;
  }
  * { margin: 0; padding: 0; box-sizing: border-box; }
  html, body {
    width: 1200px; height: 884px; overflow: hidden;
    background: var(--stage);
  }
  .canvas { position: relative; width: 1200px; height: 884px; }

  .panel {
    position: absolute; top: 117px; height: 650px; overflow: hidden;
    background: radial-gradient(ellipse at 55% 40%, var(--panel-mid) 0%, var(--panel-dark) 80%);
  }

  /* ---------- side panel ---------- */
  .side-panel {
    left: 190px; width: 140px;
    border-right: 2px solid var(--fold);
    background: linear-gradient(90deg, var(--panel-dark) 0%, #262626 100%);
  }
  .side-tag {
    position: absolute; left: 22px; top: 30px;
    width: 32px; height: 360px;
    background: linear-gradient(90deg, var(--banner-red) 0%, var(--banner-red-dark) 100%);
    writing-mode: vertical-rl;
    display: flex; align-items: center; justify-content: flex-end;
    padding-bottom: 14px;
    font-family: "Roboto Condensed", sans-serif; font-weight: 700;
    font-size: 19px; color: var(--white); text-transform: uppercase;
  }
  .side-title {
    position: absolute; left: 54px; top: 30px;
    width: 66px; height: 400px;
    background: linear-gradient(90deg, var(--banner-blue) 0%, var(--banner-blue-dark) 100%);
    border-left: 2px solid var(--silver);
    border-right: 2px solid var(--silver);
    writing-mode: vertical-rl;
    display: flex; flex-direction: column; justify-content: center;
    padding-top: 40px;
  }
  .side-title .title-line {
    font-family: "Audiowide", sans-serif;
    font-size: 23px; line-height: 29px; color: var(--silver);
    text-transform: uppercase; letter-spacing: 1px;
  }
  .side-brand {
    position: absolute; left: 50px; top: 460px;
    writing-mode: vertical-rl;
    display: flex; align-items: center; gap: 10px;
  }
  .side-brand .brand-dot { width: 30px; height: 30px; }
  .side-brand .brand-name { font-size: 24px; letter-spacing: 2px; }

  /* ---------- front panel ---------- */
  .front-panel { left: 330px; width: 700px; }

  .brand-dot {
    display: block; border-radius: 50%; background: var(--silver);
  }
  .brand-name {
    font-family: "Roboto Condensed", sans-serif; font-weight: 700;
    color: var(--silver); text-transform: uppercase;
  }
  .front-brand {
    position: absolute; left: 86px; top: 144px;
    display: flex; align-items: center; gap: 12px;
  }
  .front-brand .brand-dot { width: 32px; height: 32px; }
  .front-brand .brand-name { font-size: 38px; letter-spacing: 2px; }

  .features {
    position: absolute; left: 364px; top: 130px;
    width: 336px; height: 100px;
    background: var(--label-yellow);
    border-top: 4px solid var(--banner-blue);
    padding: 10px 0 0 18px;
    list-style: none;
  }
  .features li {
    display: flex; align-items: center; gap: 6px;
    font-family: "Roboto Condensed", sans-serif; font-weight: 700;
    font-size: 16px; line-height: 27px; color: var(--label-ink);
    text-transform: uppercase; white-space: nowrap;
  }
  .features svg { width: 18px; height: 18px; flex: none; }

  .product-photo {
    position: absolute; left: 44px; top: 270px;
    width: 238px; height: 250px; border-radius: 48% / 46%;
    border: 4px solid var(--silver);
    background: radial-gradient(ellipse at 50% 50%, var(--panel-dark) 30%, var(--shoe-light) 33%, var(--shoe-dark) 70%);
  }

  .genuine-seal {
    position: absolute; left: 490px; top: 262px;
    width: 108px; height: 108px; border-radius: 50%;
    border: 3px solid var(--silver);
  }

  .tag-banner {
    position: absolute; left: 386px; top: 400px;
    width: 314px; height: 50px;
    background: linear-gradient(180deg, var(--banner-red) 0%, var(--banner-red-dark) 100%);
    clip-path: polygon(6% 0, 100% 0, 100% 100%, 0 100%);
    display: flex; align-items: center; justify-content: center;
    font-family: "Roboto Condensed", sans-serif; font-weight: 700;
    font-size: 26px; color: var(--white); text-transform: uppercase;
    padding-left: 18px;
  }

  .title-banner {
    position: absolute; left: 248px; top: 450px;
    width: 452px; height: 114px;
    background: linear-gradient(180deg, var(--banner-blue) 0%, var(--banner-blue-dark) 100%);
    border-top: 3px solid var(--silver);
    border-bottom: 3px solid var(--silver);
    clip-path: polygon(8% 0, 100% 0, 100% 100%, 0 100%);
    display: flex; flex-direction: column; justify-content: center; align-items: center;
    padding-left: 30px;
  }
  .title-banner .title-line {
    font-family: "Audiowide", sans-serif;
    font-size: 36px; line-height: 44px; color: var(--silver);
    text-transform: uppercase; letter-spacing: 2px; white-space: nowrap;
  }
</style>
</head>
<body>
  <main class="canvas">
    <section class="panel side-panel">
      <div class="side-tag">Asbestos Free</div>
      <div class="side-title">
        <span class="title-line">Motor Cycle</span>
        <span class="title-line">Brake Shoes</span>
      </div>
      <div class="side-brand">
        <span class="brand-dot"></span>
        <span class="brand-name">Vorenta</span>
      </div>
    </section>

    <section class="panel front-panel">
      <div class="front-brand">
        <span class="brand-dot"></span>
        <span class="brand-name">Vorenta</span>
      </div>

      <ul class="features">
        <li><svg viewBox="0 0 20 20"><path d="M2 11 L8 17 L18 3" fill="none" stroke="#111" stroke-width="4"/></svg>Superior Breaking System</li>
        <li><svg viewBox="0 0 20 20"><path d="M2 11 L8 17 L18 3" fill="none" stroke="#111" stroke-width="4"/></svg>Exceptional Stopping Power</li>
        <li><svg viewBox="0 0 20 20"><path d="M2 11 L8 17 L18 3" fill="none" stroke="#111" stroke-width="4"/></svg>Advance Friction Formulation</li>
      </ul>

      <div class="product-photo" role="img" aria-label="Photo of a pair of motorcycle drum brake shoes joined by springs"></div>

      <div class="genuine-seal"></div>

      <div class="tag-banner">Asbestos Free</div>

      <div class="title-banner">
        <span class="title-line">Motor Cycle</span>
        <span class="title-line">Brake Shoes</span>
      </div>
    </section>
  </main>
</body>
</html>
```